Powerpoint Sales and Pre-Sales Decks

We need a GD to support us as we start buillidng many PPT decks - we are a start-up based in London in the Telecomms space

```html
<!DOCTYPE html>
<html lang="en">
<head>
<meta charset="utf-8">
<title>Telecom Pitch Deck Slides</title>
<link href="https://fonts.googleapis.com/css2?family=Montserrat:wght@400;500;600;700&display=swap" rel="stylesheet">
<style>
:root{
  --ink:#0d4fa3;
  --sky:#1a8fd4;
  --brand:#1a73d0;
  --deep:#1f64b4;
  --royal:#0f4ea0;
  --footer:#d5dadf;
  --badge:#0a86d0;
  --text:#333;
  --muted:#8a8f96;
  --bar-dark:#4a6078;
  --bar-grey:#b5c1c2;
  --bar-blue:#1a8fd0;
  --bar-light:#4ab5e8;
}
*{margin:0;padding:0;box-sizing:border-box}
html,body{width:1200px;height:1032px;overflow:hidden;background:#000;font-family:'Montserrat',sans-serif}
.canvas{position:relative;width:1200px;height:1032px}
.slide{position:absolute;width:573px;height:322px;background:#fff;overflow:hidden}
.s1{left:8px;top:8px}.s2{left:613px;top:8px}
.s3{left:8px;top:346px}.s4{left:613px;top:346px}
.s5{left:8px;top:697px}.s6{left:613px;top:697px}
.footer{position:absolute;left:0;bottom:0;width:100%;height:14px;background:var(--footer)}
.url{position:absolute;left:6px;top:2px;font-size:8px;letter-spacing:1px;color:var(--ink)}
.page{position:absolute;right:0;top:0;width:62px;height:14px;background:var(--badge);color:#fff;font-size:6.5px;font-weight:700;text-align:center;line-height:14px}
.title{position:absolute;left:10px;top:10px;font-size:20px;font-weight:700;color:var(--ink);padding-left:6px;border-left:4px solid var(--brand);line-height:22px}
.title span{color:var(--sky)}
.logo{position:absolute;right:12px;top:10px;font-size:14px;font-weight:700;color:var(--brand)}
.ptitle{position:absolute;font-size:12px;font-weight:700;color:#1f3f7a}
.bullets{position:absolute;list-style:none}
.bullets li{position:relative;padding-left:19px;font-size:8.3px;line-height:10.6px;color:var(--text);text-align:justify;margin-bottom:15px}
.bullets li::before{content:"";position:absolute;left:3px;top:2px;width:6px;height:6px;border-radius:50%;background:var(--ink);box-shadow:0 0 0 2px #c9d6e8}
.cover-shape{position:absolute;inset:0}
.cover-logo{position:absolute;left:95px;top:184px;font-size:24px;font-weight:700;color:#fff}
.cover-title{position:absolute;left:351px;top:182px;font-size:22px;font-weight:700;color:var(--brand)}
.cover-sub{position:absolute;left:351px;font-size:11.5px;font-weight:500;color:var(--brand);letter-spacing:.5px}
.graph-title{position:absolute;left:63px;top:265px;font-size:12px;font-weight:700;color:#1f3f7a}
.graph-text{position:absolute;left:190px;top:258px;width:340px;font-size:8px;line-height:10.5px;color:var(--muted)}
.photo{position:absolute}
.feature{position:absolute;top:75px;width:160px;text-align:center}
.feature .ring{margin:0 auto;width:94px;height:94px;border-radius:50%;border:4px solid #d4d9e2;display:flex;align-items:center;justify-content:center}
.feature .disc{width:80px;height:80px;border-radius:50%;background:var(--royal);display:flex;align-items:center;justify-content:center}
.feature h3{margin-top:14px;font-size:12px;font-weight:700;color:#1f3f7a}
.feature p{margin-top:4px;font-size:8.3px;line-height:10.6px;color:var(--text);padding:0 6px}
.section-title{position:absolute;left:28px;top:230px;font-size:25px;font-weight:700;color:#fff}
.s6 .logo{color:#fff}
</style>
</head>
<body>
<div class="canvas">

  <section class="slide s1">
    <div class="photo" role="img" aria-label="Satellite dish photograph tinted blue" style="inset:0"></div>
    <svg class="cover-shape" width="573" height="322" viewBox="0 0 573 322">
      <defs>
        <linearGradient id="coverBlue" x1="0" y1="0" x2="1" y2="1">
          <stop offset="0" stop-color="#1f78d8"/><stop offset="1" stop-color="#0d5cc0"/>
        </linearGradient>
      </defs>
      <polygon points="0,0 234,0 354,308 0,308" fill="url(#coverBlue)" role="img" aria-label="Satellite dish photograph in blue tint"/>
    </svg>
    <div class="cover-logo">LOGO Here</div>
    <div class="cover-title">Project Title here</div>
    <div class="cover-sub" style="top:218px">Subtext paragraph here</div>
    <div class="cover-sub" style="top:241px">Author name : ZYX</div>
    <div class="footer"><span class="url">www.orbitline.co</span><span class="page">Page : 01</span></div>
  </section>

  <section class="slide s2">
    <h2 class="title">Project <span>Title here</span></h2>
    <div class="logo" style="top:8px">LOGO Here</div>
    <svg style="position:absolute;left:0;top:0" width="573" height="260" viewBox="0 0 573 260" font-family="Montserrat, sans-serif" font-size="8" fill="#999">
      <g stroke="#e3e6ea" stroke-width="1">
        <line x1="68" y1="57" x2="530" y2="57"/><line x1="68" y1="98" x2="530" y2="98"/>
        <line x1="68" y1="139" x2="530" y2="139"/><line x1="68" y1="180" x2="530" y2="180"/>
        <line x1="68" y1="221" x2="530" y2="221"/>
      </g>
      <g text-anchor="end">
        <text x="68" y="55">100</text><text x="68" y="96">75</text><text x="68" y="137">50</text>
        <text x="68" y="178">25</text><text x="68" y="219">0</text>
      </g>
      <rect x="85" y="155" width="20" height="66" fill="var(--bar-dark)"/>
      <rect x="122" y="106" width="20" height="115" fill="var(--bar-grey)"/>
      <rect x="159" y="123" width="20" height="98" fill="var(--bar-blue)"/>
      <rect x="196" y="95" width="20" height="126" fill="var(--bar-light)"/>
      <rect x="233" y="128" width="20" height="93" fill="var(--bar-dark)"/>
      <rect x="270" y="106" width="20" height="115" fill="var(--bar-grey)"/>
      <rect x="307" y="114" width="20" height="107" fill="var(--bar-blue)"/>
      <rect x="344" y="65" width="20" height="156" fill="var(--bar-light)"/>
      <rect x="381" y="98" width="20" height="123" fill="var(--bar-dark)"/>
      <rect x="418" y="78" width="20" height="143" fill="var(--bar-grey)"/>
      <rect x="455" y="111" width="20" height="110" fill="var(--bar-blue)"/>
      <rect x="492" y="90" width="20" height="131" fill="var(--bar-light)"/>
      <g text-anchor="middle">
        <text x="95" y="242">JAN</text><text x="132" y="242">FEB</text><text x="169" y="242">MAR</text>
        <text x="206" y="242">APR</text><text x="243" y="242">MAY</text><text x="280" y="242">JUN</text>
        <text x="317" y="242">JUL</text><text x="354" y="242">AUG</text><text x="391" y="242">SEP</text>
        <text x="428" y="242">OCT</text><text x="465" y="242">NOV</text><text x="502" y="242">DEC</text>
      </g>
    </svg>
    <div class="graph-title">Graphs Title here</div>
    <p class="graph-text">sed diam nonummy nibh euismod tincidunt ut laoreet dolore magna aliquam erat volutpat. Ut wisi enim ad minim veniam, quis nostrud exerci tation ullamcorper suscipit lobortis nisl ut aliquip ex ea commodo</p>
    <div class="footer"><span class="page">Page : 01</span></div>
  </section>

  <section class="slide s3">
    <h2 class="title">Project <span>Title here</span></h2>
    <div class="logo" style="top:9px">LOGO Here</div>
    <div class="ptitle" style="left:19px;top:76px">Paragraph Title here</div>
    <ul class="bullets" style="left:19px;top:98px;width:280px">
      <li>sed diam nonummy nibh euismod tincidunt ut laoreet dolore magna aliquam erat volutpat. Ut wisi enim ad minim veniam, quis nostrud exerci tation ullamcorper suscipit lobortis nisl ut aliquip ex ea commodo consequat</li>
      <li>sed diam nonummy nibh euismod tincidunt ut laoreet dolore magna aliquam erat volutpat. Ut wisi enim ad minim veniam, quis nostrud exerci tation ullamcorper suscipit lobortis nisl ut aliquip ex ea commodo consequat</li>
      <li style="margin-top:21px">sed diam nonummy nibh euismod tincidunt ut laoreet dolore magna aliquam erat volutpat. Ut wisi enim ad minim veniam, quis nostrud exerci tation ullamcorper suscipit lobortis nisl ut aliquip ex ea commodo consequat</li>
    </ul>
    <div class="photo" role="img" aria-label="Satellite dish in front of a blue networked globe" style="left:316px;top:53px;width:244px;height:243px;background:linear-gradient(135deg,#2a7fe0,#7cc0f4 55%,#cfe6fb)"></div>
    <div class="footer"><span class="url">www.orbitline.co</span><span class="page">Page : 01</span></div>
  </section>

  <section class="slide s4">
    <h2 class="title">Project <span>Title here</span></h2>
    <div class="logo">LOGO Here</div>
    <div class="feature" style="left:26px">
      <div class="ring"><div class="disc">
        <svg width="46" height="34" viewBox="0 0 46 34" fill="none" stroke="#fff" stroke-width="1.6" stroke-linejoin="round"><path d="M4 12h8l14-8v24l-14-8H4z"/><path d="M8 20l3 10h4l-2-10"/><path d="M32 10l6-4M33 16h8M32 22l6 4"/></svg>
      </div></div>
      <h3>Paragraph Title here</h3>
      <p>sed diam nonummy nibh euismod tincidunt ut laoreet dolore magna aliquam erat volutpat. Ut wisi enim ad minim veniam, quis nostrud exerci tation ullamcorper suscipit lobortis nisl ut aliquip ex ea commodo</p>
    </div>
    <div class="feature" style="left:202px">
      <div class="ring"><div class="disc">
        <svg width="42" height="36" viewBox="0 0 42 36" fill="none" stroke="#fff" stroke-width="1.6"><rect x="3" y="3" width="36" height="24" rx="2"/><path d="M17 27l-2 6h12l-2-6"/><path d="M10 11h22M10 16h22M10 21h14"/></svg>
      </div></div>
      <h3>Paragraph Title here</h3>
      <p>sed diam nonummy nibh euismod tincidunt ut laoreet dolore magna aliquam erat volutpat. Ut wisi enim ad minim veniam, quis nostrud exerci tation ullamcorper suscipit lobortis nisl ut aliquip ex ea commodo</p>
    </div>
    <div class="feature" style="left:378px">
      <div class="ring"><div class="disc">
        <svg width="42" height="36" viewBox="0 0 42 36" fill="none" stroke="#fff" stroke-width="1.6"><path d="M3 33h36"/><rect x="8" y="22" width="5" height="11"/><rect x="17" y="17" width="5" height="16"/><rect x="26" y="11" width="5" height="22"/><path d="M6 18l9-7 6 4 12-11M28 4h5v5"/></svg>
      </div></div>
      <h3>Paragraph Title here</h3>
      <p>sed diam nonummy nibh euismod tincidunt ut laoreet dolore magna aliquam erat volutpat. Ut wisi enim ad minim veniam, quis nostrud exerci tation ullamcorper suscipit lobortis nisl ut aliquip ex ea commodo</p>
    </div>
    <div class="footer"><span class="url">www.orbitline.co</span><span class="page">Page : 01</span></div>
  </section>

  <section class="slide s5">
    <h2 class="title">Project <span>Title here</span></h2>
    <div class="logo" style="font-size:16px">LOGO Here</div>
    <div class="ptitle" style="left:19px;top:75px">Paragraph Title here</div>
    <ul class="bullets" style="left:19px;top:98px;width:262px">
      <li>sed diam nonummy nibh euismod tincidunt ut laoreet dolore magna aliquam erat volutpat. Ut wisi enim ad minim veniam, quis nostrud exerci tation ullamcorper suscipit lobortis nisl ut aliquip ex ea commodo consequat</li>
      <li>sed diam nonummy nibh euismod tincidunt ut laoreet dolore magna aliquam erat volutpat. Ut wisi enim ad minim veniam, quis nostrud exerci tation ullamcorper suscipit lobortis nisl ut aliquip ex ea commodo consequat</li>
      <li style="margin-top:21px">sed diam nonummy nibh euismod tincidunt ut laoreet dolore magna aliquam erat volutpat. Ut wisi enim ad minim veniam, quis nostrud exerci tation ullamcorper suscipit lobortis nisl ut aliquip ex ea commodo consequat</li>
    </ul>
    <div class="ptitle" style="left:301px;top:75px">Paragraph Title here</div>
    <ul class="bullets" style="left:301px;top:98px;width:262px">
      <li>sed diam nonummy nibh euismod tincidunt ut laoreet dolore magna aliquam erat volutpat. Ut wisi enim ad minim veniam, quis nostrud exerci tation ullamcorper suscipit lobortis nisl ut aliquip ex ea commodo consequat</li>
      <li>sed diam nonummy nibh euismod tincidunt ut laoreet dolore magna aliquam erat volutpat. Ut wisi enim ad minim veniam, quis nostrud exerci tation ullamcorper suscipit lobortis nisl ut aliquip ex ea commodo consequat</li>
      <li style="margin-top:21px">sed diam nonummy nibh euismod tincidunt ut laoreet dolore magna aliquam erat volutpat. Ut wisi enim ad minim veniam, quis nostrud exerci tation ullamcorper suscipit lobortis nisl ut aliquip ex ea commodo consequat</li>
    </ul>
    <div class="footer"><span class="url">www.orbitline.co</span><span class="page">Page : 01</span></div>
  </section>

  <section class="slide s6">
    <div class="photo" role="img" aria-label="Telecom tower with antennas against a cloudy sky" style="inset:0;background:linear-gradient(180deg,#9fb3cc,#c3cfdc 60%,#aab9cc)"></div>
    <svg style="position:absolute;left:0;top:0" width="573" height="322" viewBox="0 0 573 322">
      <polygon points="0,78 540,308 0,308" fill="var(--deep)"/>
      <polygon points="573,142 350,222 540,308 573,308" fill="#0a74d4"/>
      <rect x="75" y="117" width="14" height="22" fill="#0c56b0"/>
    </svg>
    <div class="logo" style="top:13px;font-size:14px">LOGO Here</div>
    <div class="section-title">SECTION TITLE HERE</div>
    <div class="footer"><span class="url">www.orbitline.co</span><span class="page">Page : 01</span></div>
  </section>

</div>
</body>
</html>
```